Awsome new website

We are a Fencing Contracting company in Melbourne Australia. We supply and install Timer and Steel boundary fences as well as Pool fencing (e.g. glass, tubular steel). We also manufacture and install swing and sliding gates.

We want a new website that is a modern business website.
We are targeting domestic and business clients.
The design should compliment our logo and company name.
The website needs to be easy to update.

Some specifics we want.
Menu - Main menu at top of page and smaller footer menu (to add different menu items)
Slider - Main page to have a slider on it that's easy for us to add and remove slides.
Call to action - all pages to have a "call to action" logo or icon that attracts attention (see file "call_to_action.pdf)
Instant quote - we have a online quote page we need a distinctive logo or icon to redirect to this page.
Main page to have a product /Service guide (see file "website_idea.jpg")
Main page to have widgets or quick link to
o why choose us
o Brochures
o Gallery

Have a Gallery page formatted with different category galleries. e.g. Timber, Glass, Feature
Maintain the current link to our staff page with password, (link in footer menu)

Hopefully that covers everything.
Our current website is www.tallwattlefencing.com.au to have a look at the current site.
regards Doug

• Turn off blogging as we don’t want 100’s of comments from spammers to delete

We would like to implement the PortalNest plugin (see "http://portalnest-example.com/" ), but this can be done after the new Theme has been implemented.

```html
<!DOCTYPE html>
<html lang="en">
<head>
<meta charset="utf-8">
<title>Tall Wattle Fencing</title>
<link rel="stylesheet" href="https://fonts.googleapis.com/css2?family=PT+Sans:wght@400;700&display=swap">
<style>
:root{
  --red:#8e1116;
  --red-dark:#6e0a0e;
  --text:#8a8a8a;
  --line:#d9d9d9;
  --white:#fff;
  --blue:#1a8fe0;
  --footer:#0c0c0c;
  --grass:#6d8a4e;
}
*{box-sizing:border-box;margin:0;padding:0}
html,body{width:955px;height:1200px;overflow:hidden;background:var(--white)}
body{position:relative;font-family:"PT Sans",Arial,sans-serif;color:var(--text)}
.abs{position:absolute}

.brand{left:69px;top:32px;width:190px;height:55px;display:flex;align-items:center;gap:8px;color:var(--red);font-weight:700;font-size:17px;line-height:1;white-space:nowrap}
.brand-mark{width:14px;height:14px;background:var(--red);flex:none}
.search{left:678px;top:47px;width:207px;height:28px;border:1px solid #cfcfcf;font-size:12px;color:#777;padding:6px 10px;display:flex;justify-content:space-between;align-items:center}

.main-nav{left:0;top:105px;width:955px;height:38px;background:linear-gradient(#b71d22,var(--red-dark));border-top:1px solid #7a0c10;display:flex;padding-left:69px}
.main-nav a{display:flex;align-items:center;justify-content:center;color:var(--white);text-decoration:none;font-size:13px;font-weight:700;border-right:1px solid #6a080c;box-shadow:1px 0 0 #b8353a}
.main-nav a:last-child{border-right:0;box-shadow:none}

.hero{left:0;top:143px;width:955px;height:342px;background:linear-gradient(180deg,#4c6b3a 0%,#5d7c42 30%,var(--grass) 55%,#4e6a38 100%)}
.hero-caption{left:69px;top:398px;width:644px;height:61px;background:rgba(40,40,40,.78);display:flex;align-items:center;padding-left:16px}
.hero-caption h2{color:var(--white);font-size:19px;font-weight:400;letter-spacing:.2px;white-space:nowrap}
.subscribe{left:543px;top:411px;width:159px;height:38px;background:var(--blue);color:var(--white);font-size:15px;display:flex;align-items:center;gap:8px;padding-left:12px;white-space:nowrap}
.dots{left:846px;top:463px;display:flex;gap:3px}
.dots i{width:8px;height:8px;border-radius:50%;border:1px solid #ccc;background:#666}
.dots i:first-child{background:#fff}

.heading{color:var(--red);font-size:16px;font-weight:400}
.body-copy{font-size:12.5px;line-height:23px;color:var(--text)}
.services-list{left:69px;top:645px;width:520px;font-size:12.5px;display:grid;grid-template-columns:197px 150px 173px;row-gap:12px}
.services-list li{list-style:none;display:flex;align-items:center;gap:9px;white-space:nowrap}
.rule{left:69px;top:746px;width:502px;height:1px;background:var(--line)}

.thumb{width:154px;height:122px;border:4px solid var(--white);box-shadow:0 0 3px rgba(0,0,0,.35)}

.quote-box{left:620px;top:516px;width:265px;height:336px;background:var(--white);box-shadow:0 0 5px rgba(0,0,0,.25)}
.field{left:639px;width:226px;height:30px;border:1px solid #d6d6d6;box-shadow:inset 0 1px 2px rgba(0,0,0,.08);font-size:11px;color:#888;padding:8px 9px}
.submit{left:781px;top:805px;width:83px;height:26px;background:var(--red);color:var(--white);font-size:13.5px;display:flex;align-items:center;justify-content:center}
.brochure{left:619px;top:881px;width:266px;height:44px;background:linear-gradient(#3e3e3e,#232323);color:var(--white);font-size:15.5px;display:flex;align-items:center;padding-left:19px;gap:35px;white-space:nowrap}
.brochure-icon{width:26px;height:30px;background:#e8e8e8;border-radius:2px;flex:none}

.footer{left:0;top:1113px;width:955px;height:87px;background:var(--footer)}
.footer-links{left:69px;top:1134px;font-size:11px;color:var(--white);white-space:nowrap}
.copyright{left:69px;top:1161px;font-size:11px;color:var(--white)}
.social{top:1141px;width:30px;height:30px}
</style>
</head>
<body>

<header>
  <div class="abs brand"><span class="brand-mark"></span>Tall Wattle Fencing</div>
  <div class="abs search"><span>Search..</span>
    <svg width="12" height="12" viewBox="0 0 12 12"><circle cx="5" cy="5" r="3.6" fill="none" stroke="#999" stroke-width="1.6"/><line x1="7.6" y1="7.6" x2="11" y2="11" stroke="#999" stroke-width="1.8"/></svg>
  </div>
  <nav class="abs main-nav">
    <a style="width:85px">HOME</a>
    <a style="width:122px">TUFFPANEL</a>
    <a style="width:144px">INSTANT QUOTE</a>
    <a style="width:99px">GALLERY</a>
    <a style="width:113px">PRODUCTS</a>
    <a style="width:133px">OUR SERVICES</a>
    <a style="width:123px">CONTACT US</a>
  </nav>
</header>

<section>
  <div class="abs hero" role="img" aria-label="Black steel boundary fence in front of a green lawn with trees"></div>
  <div class="abs hero-caption"><h2>NAM LIBER TEMPOR CUM SOLUTA NOBIS ELEIFD</h2></div>
  <div class="abs subscribe">
    <svg width="20" height="22" viewBox="0 0 20 22"><path d="M14 2 L6 12 L10 12 L4 20" fill="none" stroke="#fff" stroke-width="1.6"/><path d="M4 20 L4 15 M4 20 L9 19" stroke="#fff" stroke-width="1.6"/></svg>
    SUBSCRIBE HERE</div>
  <div class="abs dots"><i></i><i></i><i></i><i></i></div>
</section>

<main>
  <h3 class="abs heading" style="left:69px;top:512px">Our Services</h3>
  <p class="abs body-copy" style="left:69px;top:542px;width:504px;word-break:break-all">We offer a 12 month workmanshhttp://tallwattlefencing.com.au/images/bt-arise/aboutus.jpgip warranty on our fences and wll clean the site for free of any debris from the fence construction upon completion of the job. We can offer this workmanship warranty because of our work practices, these include</p>
  <ul class="abs services-list">
    <li><svg width="11" height="11"><circle cx="5.5" cy="5.5" r="5.5" fill="#999"/><path d="M4 3 L7 5.5 L4 8" fill="none" stroke="#fff" stroke-width="1.4"/></svg>Bathroom Remodeling</li>
    <li><svg width="11" height="11"><circle cx="5.5" cy="5.5" r="5.5" fill="#999"/><path d="M4 3 L7 5.5 L4 8" fill="none" stroke="#fff" stroke-width="1.4"/></svg>Tile &amp; Flooring</li>
    <li><svg width="11" height="11"><circle cx="5.5" cy="5.5" r="5.5" fill="#999"/><path d="M4 3 L7 5.5 L4 8" fill="none" stroke="#fff" stroke-width="1.4"/></svg>Genral Home Maintenance</li>
    <li><svg width="11" height="11"><circle cx="5.5" cy="5.5" r="5.5" fill="#999"/><path d="M4 3 L7 5.5 L4 8" fill="none" stroke="#fff" stroke-width="1.4"/></svg>Attic &amp; Garage Finishing</li>
    <li><svg width="11" height="11"><circle cx="5.5" cy="5.5" r="5.5" fill="#999"/><path d="M4 3 L7 5.5 L4 8" fill="none" stroke="#fff" stroke-width="1.4"/></svg>Decks</li>
    <li><svg width="11" height="11"><circle cx="5.5" cy="5.5" r="5.5" fill="#999"/><path d="M4 3 L7 5.5 L4 8" fill="none" stroke="#fff" stroke-width="1.4"/></svg>Painting &amp; Wall Treatments</li>
    <li><svg width="11" height="11"><circle cx="5.5" cy="5.5" r="5.5" fill="#999"/><path d="M4 3 L7 5.5 L4 8" fill="none" stroke="#fff" stroke-width="1.4"/></svg>Carpentry</li>
    <li><svg width="11" height="11"><circle cx="5.5" cy="5.5" r="5.5" fill="#999"/><path d="M4 3 L7 5.5 L4 8" fill="none" stroke="#fff" stroke-width="1.4"/></svg>Fences</li>
    <li><svg width="11" height="11"><circle cx="5.5" cy="5.5" r="5.5" fill="#999"/><path d="M4 3 L7 5.5 L4 8" fill="none" stroke="#fff" stroke-width="1.4"/></svg>Drywall Install</li>
  </ul>
  <div class="abs rule"></div>

  <h3 class="abs heading" style="left:69px;top:765px">Photo Gallery</h3>
  <div class="abs thumb" style="left:71px;top:797px;background:linear-gradient(#3d5a2a,#8a6a3e)" role="img" aria-label="Timber picket fence and gate in a garden"></div>
  <div class="abs thumb" style="left:244px;top:797px;background:linear-gradient(#5a3f2c,#3a2418)" role="img" aria-label="Dark timber floor with light inlay"></div>
  <div class="abs thumb" style="left:416px;top:797px;background:linear-gradient(#b06a2c,#7a3e18)" role="img" aria-label="Curved timber balcony railing"></div>
  <div class="abs thumb" style="left:71px;top:944px;background:linear-gradient(#6a5a3a,#b8782e)" role="img" aria-label="Timber deck with pergola"></div>
  <div class="abs thumb" style="left:244px;top:944px;background:linear-gradient(#8a8a8a,#c8743a)" role="img" aria-label="Electrical conduit installation"></div>
  <div class="abs thumb" style="left:416px;top:944px;background:linear-gradient(90deg,#7a0e10,#c63a44)" role="img" aria-label="Red feature wall interior"></div>
</main>

<aside>
  <div class="abs quote-box"></div>
  <h3 class="abs heading" style="left:639px;top:535px;font-size:14.5px">ONLINE QUOTE</h3>
  <div class="abs field" style="top:566px">Full Name</div>
  <div class="abs field" style="top:604px">Phone Number</div>
  <div class="abs field" style="top:641px">Email Address</div>
  <div class="abs field" style="top:679px">Cit/Zip Code</div>
  <div class="abs field" style="top:718px">Fence Type</div>
  <div class="abs field" style="top:758px">Fence Cost</div>
  <div class="abs submit">SUBMIT</div>

  <div class="abs brochure"><span class="brochure-icon"></span>Download Our Brochure</div>

  <h3 class="abs heading" style="left:619px;top:949px">Why choose us?</h3>
  <p class="abs body-copy" style="left:619px;top:978px;width:268px;font-size:12px;word-break:break-all">At Tall Wattle Fencing, we believe in quality above all. The first fence we constructed was over 25 years ago and the number one thing we have learnt is that to do the job right the first time is the best.</p>
</aside>

<footer>
  <div class="abs footer"></div>
  <div class="abs footer-links">Home | Tuffpanel | Instant Quote | Gallery | Products &amp; Services | Contact</div>
  <div class="abs copyright">Copyrights 2013. All Rights Reserved.</div>
  <div class="abs social" style="left:702px;background:#3b5a9a"></div>
  <div class="abs social" style="left:741px;background:#2a9fd6"></div>
  <div class="abs social" style="left:779px;background:#f06a1e"></div>
  <div class="abs social" style="left:819px;background:#d9272e"></div>
</footer>

</body>
</html>
```